General Contractors need a new Crisp updated Card Design

We need a new business card design for our company of 25 years based in Toronto call Holvaster Building Inc. : Our goal is to be the leading commercial contractors in Toronto by providing exceptional value to our clients. We work very hard to deliver professional, quality, service in conjunction with consistent price competitiveness to all of our clients on every single project.

Target Market(s)

Design & Build Clients

Industry/Entity Type

Construction Company

Contact Information for Business Card

Address:
18 North Tamlin Glen Road, Unit 57, Marbrook Vale, ON, K7T 2R9
Office: 905-218-5937

Holvasters Logo
Employee Job Description
Employee Cell Phone #
Employee Email
www.holvaster-example.com

Colors

Designer to choose colors to be used in the design.

Requirements
Must have
• Quote Company Saying:
• "Professional. Quality. Service."
Nice to have
• New Crisp up to date look. simple & fresh ( Not to Busy)
Should not have
• NO BLUE PRINTS ON THE BUSINESS CARDS

```html
<!DOCTYPE html>
<html lang="en">
<head>
<meta charset="utf-8">
<title>Holvaster Building Inc. – Business Card</title>
<link rel="stylesheet" href="https://fonts.googleapis.com/css2?family=Arimo:wght@400;700&display=swap">
<style>
  :root {
    --teal: #00937f;
    --teal-deep: #007a6a;
    --teal-light: #00a58f;
    --charcoal: #2e3033;
    --paper: #f5f5f3;
    --paper-shade: #e9e9e6;
    --stage: #dcd9d3;
    --ink-white: #ffffff;
    --rule: rgba(255,255,255,0.75);
  }
  * { box-sizing: border-box; margin: 0; padding: 0; }
  html, body { width: 1200px; height: 780px; overflow: hidden; }
  body {
    background: var(--stage);
    font-family: "Arimo", Arial, sans-serif;
    position: relative;
  }
  .card {
    position: absolute;
    top: 236px;
    width: 540px;
    height: 309px;
    overflow: hidden;
    box-shadow: 0 8px 24px rgba(0,0,0,0.18);
  }
  .card--front { left: 40px; background: var(--paper); }
  .card--back  { left: 620px; background: radial-gradient(ellipse at 60% 35%, var(--teal-light), var(--teal-deep)); }

  /* front */
  .front-brand {
    position: absolute; left: 0; top: 0; width: 100%; height: 150px;
    background: linear-gradient(180deg, var(--paper), var(--paper-shade));
    display: flex; align-items: center; justify-content: center; gap: 16px;
  }
  .brand-square { width: 48px; height: 48px; background: var(--teal); }
  .brand-name {
    font-weight: 700; font-size: 34px; color: var(--teal);
    letter-spacing: 0.5px; text-transform: uppercase; line-height: 1;
  }
  .front-contact {
    position: absolute; left: 0; top: 150px; width: 100%; height: 112px;
    background: var(--teal);
    display: flex; align-items: center; padding: 0 34px;
    color: var(--ink-white);
  }
  .person { width: 200px; text-align: right; padding-right: 22px; }
  .person-name { font-weight: 700; font-size: 17px; text-transform: uppercase; }
  .person-title { font-size: 14px; margin-top: 2px; }
  .person-cell { font-size: 14px; margin-top: 6px; display: flex; justify-content: flex-end; align-items: center; gap: 6px; }
  .divider { width: 1px; height: 66px; background: var(--rule); }
  .details { padding-left: 22px; display: flex; flex-direction: column; gap: 6px; font-size: 14px; }
  .detail { display: flex; align-items: center; gap: 8px; }
  .icon { width: 16px; height: 16px; flex: none; }
  .address-strip {
    position: absolute; left: 0; bottom: 0; width: 100%; height: 47px;
    background: var(--charcoal); border-top: 2px solid var(--rule);
    color: var(--ink-white); font-size: 14px;
    display: flex; align-items: center; justify-content: center;
  }

  /* back */
  .back-brand {
    position: absolute; left: 0; top: 0; width: 100%; height: 262px;
    display: flex; flex-direction: column; align-items: center; justify-content: center; gap: 22px;
    color: var(--ink-white);
  }
  .back-mark { display: flex; align-items: center; gap: 16px; }
  .back-mark .brand-square { background: transparent; border: 2px solid var(--ink-white); }
  .back-mark .brand-name { color: var(--ink-white); }
  .tagline { font-size: 14px; letter-spacing: 3px; text-transform: uppercase; }
  .web-strip {
    position: absolute; left: 0; bottom: 0; width: 100%; height: 47px;
    background: var(--charcoal); border-top: 2px solid var(--rule);
    color: var(--ink-white); font-size: 14px; letter-spacing: 2px;
    display: flex; align-items: center; justify-content: center;
  }
</style>
</head>
<body>
  <section class="card card--front" aria-label="Business card front">
    <div class="front-brand">
      <span class="brand-square" aria-hidden="true"></span>
      <span class="brand-name">Holvaster Building Inc.</span>
    </div>
    <div class="front-contact">
      <div class="person">
        <div class="person-name">Marcus Ellery</div>
        <div class="person-title">Director</div>
        <div class="person-cell">905-440-2716
          <svg class="icon" viewBox="0 0 16 16" aria-hidden="true"><circle cx="8" cy="8" r="7.2" fill="none" stroke="#fff" stroke-width="1.2"/><rect x="5.5" y="3.5" width="5" height="9" rx="1" fill="none" stroke="#fff" stroke-width="1.1"/></svg>
        </div>
      </div>
      <div class="divider"></div>
      <div class="details">
        <div class="detail">
          <svg class="icon" viewBox="0 0 16 16" aria-hidden="true"><circle cx="8" cy="8" r="7.2" fill="none" stroke="#fff" stroke-width="1.2"/><path d="M5 4.5c0 4 2.5 6.5 6.5 7l.8-1.6-1.8-1-1 .8c-1.2-.5-2-1.3-2.4-2.4l.8-1-1-1.8z" fill="#fff"/></svg>
          905-218-5937
        </div>
        <div class="detail">
          <svg class="icon" viewBox="0 0 16 16" aria-hidden="true"><circle cx="8" cy="8" r="7.2" fill="none" stroke="#fff" stroke-width="1.2"/><rect x="4" y="5.2" width="8" height="5.6" fill="none" stroke="#fff" stroke-width="1.1"/><path d="M4 5.4l4 3 4-3" fill="none" stroke="#fff" stroke-width="1.1"/></svg>
          info@holvaster-example.com
        </div>
        <div class="detail">
          <svg class="icon" viewBox="0 0 16 16" aria-hidden="true"><circle cx="8" cy="8" r="7.2" fill="none" stroke="#fff" stroke-width="1.2"/><circle cx="8" cy="8" r="4" fill="none" stroke="#fff" stroke-width="1"/><path d="M4 8h8M8 4v8" stroke="#fff" stroke-width="1"/></svg>
          www.holvaster-example.com
        </div>
      </div>
    </div>
    <div class="address-strip">18 North Tamlin Glen Road, Unit 57, Marbrook Vale, ON, K7T 2R9</div>
  </section>

  <section class="card card--back" aria-label="Business card back">
    <div class="back-brand">
      <div class="back-mark">
        <span class="brand-square" aria-hidden="true"></span>
        <span class="brand-name">Holvaster Building Inc.</span>
      </div>
      <p class="tagline">Professional. Quality. Service</p>
    </div>
    <div class="web-strip">www.holvaster-example.com</div>
  </section>
</body>
</html>
```